Brightwell Amusements Investor Brochure

Start Up Company Brightwell Amusements requires 4 page A4 size brochure outlining and detailing new product. Draft layout attached. Information and points of difference included. Company logo and graphics attached. Final design should sell to investors.

```html
<!DOCTYPE html>
<html lang="en">
<head>
<meta charset="utf-8">
<title>Movies in Hospitals – Brightwell Amusements</title>
<link rel="stylesheet" href="https://fonts.googleapis.com/css2?family=Barlow+Semi+Condensed:wght@500;600;700&family=Barlow+Condensed:wght@400;500&display=swap">
<style>
  :root {
    --teal: #14a8b0;
    --blue: #4a7cc6;
    --blue-deep: #2a66b3;
    --yellow: #ffe000;
    --grey-panel: #e6e6e7;
    --grey-strip: #f5f5f5;
    --ink: #1a1a1a;
    --white: #ffffff;
    --line: #3a3a3a;
  }
  * { margin: 0; padding: 0; box-sizing: border-box; }
  html, body { width: 849px; height: 1200px; overflow: hidden; background: var(--white); }
  .page { position: relative; width: 849px; height: 1200px; background: var(--white); font-family: "Barlow Semi Condensed", sans-serif; }

  .header { position: absolute; left: 40px; top: 40px; width: 768px; height: 250px; background: var(--grey-panel); }
  .header__strip { position: absolute; left: 0; top: 77px; width: 100%; height: 68px; background: var(--grey-strip); }
  .header__title { position: absolute; left: 0; top: 76px; width: 100%; text-align: center; color: var(--teal); font-size: 64px; font-weight: 600; letter-spacing: 2.5px; line-height: 70px; white-space: nowrap; }
  .header__tagline { position: absolute; left: 0; width: 100%; text-align: center; color: var(--blue); font-size: 29px; font-weight: 700; letter-spacing: 0.8px; line-height: 34px; white-space: nowrap; }
  .header__tagline--one { top: 149px; }
  .header__tagline--two { top: 194px; }

  .hero-photo { position: absolute; left: 40px; top: 290px; width: 768px; height: 278px; background: linear-gradient(180deg, #c9c7c4 0%, #9aa0a8 45%, #5d6470 70%, #3f4650 100%); }

  .lower { position: absolute; left: 40px; top: 568px; width: 768px; height: 562px; background: linear-gradient(180deg, #e9e9eb 0%, #f4f4f6 60%, #ffffff 100%); }
  .deco-lines { position: absolute; left: 0; top: 0; }

  .kiosk-photo { position: absolute; left: 55px; top: 676px; width: 265px; height: 442px; background: linear-gradient(180deg, #6a98d6 0%, #4a7cc6 50%, #3a5f99 100%); }

  .stats { position: absolute; left: 256px; top: 655px; width: 516px; }
  .stats__title { text-align: right; color: var(--blue-deep); font-size: 19px; font-weight: 700; line-height: 23px; margin-bottom: 10px; padding-right: 2px; }
  .stats__table { width: 100%; border-collapse: separate; border-spacing: 3px 2px; margin-left: -3px; font-family: "Barlow Condensed", sans-serif; font-size: 12px; color: var(--ink); }
  .stats__table td, .stats__table th { height: 20.5px; padding: 0 4px; font-weight: 400; text-align: center; }
  .stats__table .label { text-align: left; width: 142px; }
  .stats__table th { color: var(--white); }
  .row--teal td, .row--teal th { background: var(--teal); }
  .row--teal td { color: var(--white); }
  .row--yellow td { background: var(--yellow); }

  .brand { position: absolute; left: 528px; top: 1034px; display: flex; align-items: center; gap: 12px; white-space: nowrap; }
  .brand__mark { width: 44px; height: 44px; background: var(--blue); flex: none; }
  .brand__name { font-size: 25px; font-weight: 700; color: var(--blue-deep); letter-spacing: 0.3px; }

  .player-bar { position: absolute; left: 40px; top: 1128px; width: 768px; height: 31px; background: var(--blue); }
</style>
</head>
<body>
<div class="page">

  <header class="header">
    <div class="header__strip"></div>
    <h1 class="header__title">MOVIES IN HOSPITALS</h1>
    <p class="header__tagline header__tagline--one">Download Movies in under 3 minutes</p>
    <p class="header__tagline header__tagline--two">No Internet Connection Required</p>
  </header>

  <div class="hero-photo" role="img" aria-label="Photograph of a modern hospital building with cars parked at the entrance under a cloudy sky"></div>

  <section class="lower">
    <svg class="deco-lines" width="768" height="562" viewBox="0 0 768 562" aria-hidden="true">
      <g stroke="var(--line)" stroke-width="1" fill="none">
        <line x1="0" y1="10" x2="130" y2="0"/>
        <line x1="0" y1="40" x2="260" y2="0"/>
        <line x1="0" y1="95" x2="380" y2="0"/>
        <line x1="0" y1="210" x2="320" y2="90"/>
        <line x1="160" y1="140" x2="470" y2="0"/>
      </g>
    </svg>
  </section>

  <div class="kiosk-photo" role="img" aria-label="Product photograph of the free-standing blue movie download kiosk with usage instructions"></div>

  <section class="stats">
    <h2 class="stats__title">Public and Private Hospitals,<br>States and Territories, 2012-13</h2>
    <table class="stats__table">
      <tr class="row--teal"><th class="label"></th><th>NSW</th><th>Vic</th><th>Qld</th><th>WA</th><th>SA</th><th>Tas</th><th>ACT</th><th>NT</th><th>Total</th></tr>
      <tr class="row--yellow"><td class="label">Public hospitals</td><td></td><td></td><td></td><td></td><td></td><td></td><td></td><td></td><td></td></tr>
      <tr class="row--teal"><td class="label">Public acute hospitals</td><td>218</td><td>149</td><td>166</td><td>88</td><td>78</td><td>22</td><td>3</td><td>5</td><td>729</td></tr>
      <tr class="row--yellow"><td class="label">Public psychiatric hospitals</td><td>7</td><td>1</td><td>4</td><td>2</td><td>2</td><td>1</td><td>. .</td><td>. .</td><td>17</td></tr>
      <tr class="row--teal"><td class="label">Total public hospitals</td><td>225</td><td>150</td><td>170</td><td>90</td><td>80</td><td>23</td><td>3</td><td>5</td><td>746</td></tr>
      <tr class="row--yellow"><td class="label">Private hospitals</td><td></td><td></td><td></td><td></td><td></td><td></td><td></td><td></td><td></td></tr>
      <tr class="row--teal"><td class="label">Private free-standing day</td><td>96</td><td>85</td><td>52</td><td>35</td><td>26</td><td>0</td><td>0</td><td>0</td><td>311</td></tr>
      <tr class="row--yellow"><td class="label">Other private hospitals</td><td>89</td><td>79</td><td>53</td><td>22</td><td>28</td><td>0</td><td>0</td><td>0</td><td>281</td></tr>
      <tr class="row--teal"><td class="label">Total private hospitals</td><td>185</td><td>164</td><td>105</td><td>57</td><td>54</td><td>0</td><td>0</td><td>0</td><td>592</td></tr>
      <tr class="row--yellow"><td class="label">All hospitals</td><td>410</td><td>314</td><td>275</td><td>147</td><td>134</td><td>0</td><td>0</td><td>0</td><td>1,338</td></tr>
    </table>
  </section>

  <div class="brand">
    <span class="brand__mark"></span>
    <span class="brand__name">Brightwell Amusements</span>
  </div>

  <div class="player-bar">
    <svg width="768" height="31" viewBox="0 0 768 31" aria-hidden="true">
      <polygon points="68,9 68,23 80,16" fill="var(--white)"/>
      <rect x="92" y="14" width="612" height="4" fill="#5a5a5a"/>
      <rect x="92" y="14" width="440" height="4" fill="var(--white)"/>
    </svg>
  </div>

</div>
</body>
</html>
```